Moxtrel Compensation Lawyers

We need a modern, sleek letterhead that is professional.

In relation to the footer, we would like to have firm contact details there ideally, however you must also insert at the bottom of each page the following....

Liability limited by a scheme approved under the Professional Standards Legislation.

From the attachment you can extract the firm logo. Also, I would like the Accredited specialist circle on the letterhead also.

Also, I would like you to create a document that can easily be edited for change of contact details, as these are likely to change.

Industry/Entity Type

It Professional

Font styles to use
Sans Serif

Colors
0655a3
3276b5
85abd2
0492cd
33a6d7
85cae6
cee9f5
eaf1f7
cbcbcb

Requirements
Must have
• Ph: 9317-2856
• F: 9184-3720
• M 0435-618-294
• kp@moxtrel.com.au
• www.moxtrel.com.au
Nice to have
• the word document gives you an idea of what I like. I am happy for your to amaze me with your creativity.

```html
<!DOCTYPE html>
<html lang="en">
<head>
<meta charset="utf-8">
<title>Moxtrel Compensation Lawyers — Letterhead</title>
<link rel="stylesheet" href="https://fonts.googleapis.com/css2?family=Cinzel:wght@500&family=Open+Sans:wght@400;600&display=swap">
<style>
  :root {
    --navy: #0655a3;
    --blue: #3276b5;
    --sky: #85abd2;
    --cyan: #33a6d7;
    --aqua: #85cae6;
    --ice: #cee9f5;
    --mist: #eaf1f7;
    --ink: #1f2a44;
    --backdrop: #eeeeee;
    --paper: #ffffff;
  }
  * { box-sizing: border-box; margin: 0; padding: 0; }
  html, body { width: 1200px; height: 1000px; overflow: hidden; background: var(--backdrop); }
  .letterhead {
    position: absolute; left: 270px; top: 40px; width: 660px; height: 920px;
    background: var(--paper);
    box-shadow: 0 2px 10px rgba(0,0,0,.12);
    overflow: hidden;
    font-family: "Open Sans", Arial, sans-serif;
  }
  .edge-band {
    position: absolute; top: 0; right: 0; width: 18px; height: 100%;
    background: linear-gradient(180deg, var(--aqua), var(--ice));
  }
  .watermark {
    position: absolute; left: 50%; top: 470px; transform: translate(-50%, -50%);
  }
  .masthead { position: absolute; left: 0; right: 18px; top: 48px; text-align: center; }
  .firm-name {
    display: flex; align-items: center; justify-content: center; gap: 12px;
    font-family: "Cinzel", "Times New Roman", serif; font-weight: 500;
    font-size: 19px; letter-spacing: 1.5px; color: var(--navy);
  }
  .firm-name .dot { width: 14px; height: 14px; border-radius: 50%; background: var(--cyan); }
  .contact-line {
    margin-top: 14px; display: flex; justify-content: center; gap: 26px;
    font-size: 11.5px; font-weight: 600; color: var(--ink);
  }
  .contact-line .label { color: var(--blue); }
  .postal, .web { font-size: 11.5px; color: var(--blue); margin-top: 4px; }
  .rule { height: 1px; background: var(--sky); margin: 10px 40px 0; }
  .footer { position: absolute; left: 30px; right: 48px; bottom: 34px; text-align: center; }
  .footer-rule { display: flex; align-items: center; gap: 10px; }
  .footer-rule span { flex: 1; height: 1px; background: var(--sky); }
  .footer-rule i { width: 14px; height: 14px; border-radius: 50%; background: var(--cyan); }
  .liability { margin-top: 8px; font-size: 12px; font-weight: 600; color: var(--ink); letter-spacing: .2px; }
</style>
</head>
<body>
  <main class="letterhead">
    <div class="edge-band"></div>
    <svg class="watermark" width="520" height="520" viewBox="0 0 520 520" aria-hidden="true">
      <circle cx="260" cy="260" r="250" fill="var(--mist)" opacity=".7"/>
    </svg>
    <header class="masthead">
      <div class="firm-name"><span class="dot"></span>MOXTREL COMPENSATION LAWYERS</div>
      <div class="contact-line">
        <span><span class="label">P:</span> 9317-2856</span>
        <span><span class="label">F:</span> 9184-3720</span>
        <span><span class="label">M:</span> 0435-618-294</span>
        <span><span class="label">E:</span> kp@moxtrel.com.au</span>
      </div>
      <div class="postal">P.O. Box B417 Marden Vale, South NSW 2168</div>
      <div class="web">www.moxtrel.com.au</div>
      <div class="rule"></div>
    </header>
    <footer class="footer">
      <div class="footer-rule"><span></span><i></i><span></span></div>
      <p class="liability">Liability limited by a scheme approved under the Professional Standards Legislation</p>
    </footer>
  </main>
</body>
</html>
```